Business card to be used as a flyer

This business card should do the trick of a full scale flyer , so basicaly from the business card itself we only keep the size and remove the clasical name , position , company name (etc).
This business cards should be , like said above, used as promo tool, being gived to different girls . So base one : the design is girls oriented.
Colors : black background . We will use gold (color) folio for the text.
Attached you have our logo, but this should not be a proiminent part of the design . You can use only the cat head instead.
Target Market(s)
Girls / Women
Contact Information for Business Card
> black background , gold / folio text and elements
> cat head from the logo in a creative way do be displayed
> proieminent text "your path to success starts here"
> contact details phone and website .
www.velmastrand.ro (website) and 0742163958 (phone)

```html
<!DOCTYPE html>
<html lang="en">
<head>
<meta charset="utf-8">
<title>Velmastrand – Business Card Flyer</title>
<link rel="stylesheet" href="https://fonts.googleapis.com/css2?family=Italianno&display=swap">
<style>
  :root {
    --page-bg: #fefefe;
    --card-bg: #000000;
    --gold: #f39c0b;
  }
  html, body {
    margin: 0;
    padding: 0;
    width: 1200px;
    height: 1200px;
    overflow: hidden;
    background: var(--page-bg);
  }
  .canvas {
    position: relative;
    width: 1200px;
    height: 1200px;
  }
  .card {
    position: absolute;
    left: 100px;
    top: 316px;
    width: 1007px;
    height: 575px;
    background: var(--card-bg);
    border-radius: 36px;
    color: var(--gold);
    font-family: "Italianno", cursive;
  }
  .brand-name {
    position: absolute;
    left: 0;
    right: 0;
    top: 118px;
    text-align: center;
    font-size: 58px;
    line-height: 1;
    font-weight: 400;
    color: var(--gold);
  }
  .tagline {
    position: absolute;
    left: 0;
    right: 0;
    top: 283px;
    text-align: center;
    font-size: 66px;
    line-height: 1;
    margin: 0;
    font-weight: 400;
  }
  .contact {
    position: absolute;
    left: 0;
    right: 0;
    top: 395px;
    text-align: center;
    margin: 0;
    padding: 0;
    list-style: none;
  }
  .contact-website {
    font-size: 38px;
    line-height: 44px;
  }
  .contact-phone {
    font-size: 42px;
    line-height: 44px;
    letter-spacing: 2px;
  }
</style>
</head>
<body>
  <div class="canvas">
    <section class="card">
      <div class="brand-name">Velmastrand</div>
      <h1 class="tagline">your path to success starts here</h1>
      <ul class="contact">
        <li class="contact-website">www.velmastrand.ro</li>
        <li class="contact-phone">0742163958</li>
      </ul>
    </section>
  </div>
</body>
</html>
```